Postcard Front / Back For Computer Store with IT services

We are a computer store located in Hawaii on the island of Kauai. We would like to have a post card designed to market our services that we offer. We are a PC and Notebook repair shop with full retail services.website: www.reefbyteshop.com the first thing that comes up is our service plan, we would like to market that, if you notice we have it Hawaii, meaning the background matches where we live etc, we would like to have the post card themed Hawaii.We offer a bunch of different Service contract Options for our customers:Signle computer 24.99/month Family Plan 29.99/month Business Plan 49.99/per computer month We also offer backup services much like vaultwisp but our own brand starting at 9.99/month.

website address https://www.reefbyteshop.com/online-backup/ for backup offerings..

Target Market(s)

Computer repair, IT services, Online backup, Remote Help Desk

Industry/Entity Type

Computer Repair

Requirements
Must have
• Should have front and Back color
• Phone number 808-519-3371
• website address www.reefbyteshop.com
Nice to have
• Plorin map with location on map
• Store hours mon - friday 9am - 6pm

```html
<!DOCTYPE html>
<html lang="en">
<head>
<meta charset="utf-8">
<title>ReefByte Postcard – Front and Back</title>
<link rel="stylesheet" href="https://fonts.googleapis.com/css2?family=Montserrat:wght@800&family=Questrial&family=Oswald:wght@300;400&display=swap">
<style>
  :root{
    --stage:#3b3b3b;
    --paper:#ffffff;
    --ocean:#1f7fb4;
    --ocean-dark:#17648f;
    --sky:#1fa6e4;
    --sky-pale:#cfeefb;
    --sun:#f58220;
    --ink:#333333;
    --leaf:#6f9a5a;
  }
  *{box-sizing:border-box;margin:0;padding:0}
  html,body{width:900px;height:1200px;overflow:hidden}
  body{background:var(--stage);position:relative;font-family:"Questrial",Arial,sans-serif;color:var(--ink)}

  .card{position:absolute;left:98px;width:705px;background:var(--paper);overflow:hidden}
  .card--front{top:36px;height:544px}
  .card--back{top:620px;height:546px}

  /* ---------- front ---------- */
  .tropic-scene{position:absolute;left:300px;top:0;width:405px;height:544px;
    background:linear-gradient(160deg,#e9f4ea 0%,#c8e0b8 35%,#9cbc86 60%,#eaf2dc 85%,#ffffff 100%);
    opacity:.85}
  .island-chain{position:absolute;left:255px;top:22px;width:140px;height:62px;
    background:radial-gradient(ellipse at 70% 70%,#3ba8d8 0%,#6cc4e8 45%,rgba(255,255,255,0) 72%)}
  .brand{position:absolute;display:flex;align-items:center;gap:8px}
  .brand__dot{width:22px;height:22px;border-radius:50%;background:var(--leaf)}
  .brand__name{font-family:"Montserrat",Arial,sans-serif;font-weight:800;color:var(--sky);letter-spacing:.5px}
  .card--front .brand{left:42px;top:50px}
  .card--front .brand__name{font-size:28px}

  .headline-band{position:absolute;left:0;top:127px;width:705px;height:82px;
    background:linear-gradient(90deg,var(--ocean-dark) 0%,var(--ocean) 55%,rgba(31,127,180,.25) 100%)}
  .headline{position:absolute;left:48px;top:138px;font-family:"Montserrat",Arial,sans-serif;font-weight:800;
    font-size:25px;line-height:33px;color:#fff;text-transform:uppercase;white-space:nowrap}
  .plan-tab{position:absolute;left:0;top:214px;width:335px;height:42px;background:var(--sky-pale);
    clip-path:polygon(0 0,100% 0,88% 100%,0 100%)}
  .plan-title{position:absolute;left:46px;top:220px;font-size:24px;font-weight:400;color:#1b1b1b;letter-spacing:.5px}
  .plan-title span{color:var(--sun)}

  .perks{position:absolute;left:22px;top:270px;list-style:none;font-size:15.3px;line-height:18px;color:var(--ink)}
  .perks li{position:relative;padding-left:23px;margin-bottom:6.7px}
  .perks li::before{content:"";position:absolute;left:0;top:3px;width:10px;height:10px;border:1.5px solid var(--sun);border-radius:50%}
  .perks li::after{content:"";position:absolute;left:4px;top:4.5px;width:3px;height:6px;border:solid var(--leaf);border-width:0 1.5px 1.5px 0;transform:rotate(45deg)}

  .contact-pill{position:absolute;right:28px;display:flex;align-items:center;gap:7px;color:#fff;padding-left:16px;white-space:nowrap}
  .contact-pill--phone{top:472px;width:180px;height:27px;background:var(--sun);font-size:17px;
    clip-path:polygon(6% 0,100% 0,100% 100%,0 100%)}
  .contact-pill--web{top:505px;width:182px;height:29px;background:var(--sky);font-size:14.5px;padding-left:14px;
    clip-path:polygon(6% 0,100% 0,100% 100%,0 100%)}

  /* ---------- back ---------- */
  .back-shape{position:absolute;left:0;top:0}
  .offer-intro{position:absolute;left:27px;top:20px;font-size:16.5px;line-height:22px;color:#1c1c1c;text-transform:uppercase;letter-spacing:.3px}
  .plan-row{position:absolute;left:0;height:34px;width:402px;display:flex;font-family:"Oswald",Arial,sans-serif;font-weight:400;white-space:nowrap}
  .plan-row__name{width:176px;background:var(--sky);color:#111;font-size:23px;line-height:34px;padding-left:26px;
    clip-path:polygon(0 0,100% 0,97% 100%,0 100%)}
  .plan-row__price{flex:1;background:var(--sun);color:#fff;font-size:23px;line-height:34px;padding-left:18px;margin-left:2px;
    clip-path:polygon(3% 0,100% 0,97% 100%,0 100%)}
  .plan-row--single{top:92px}
  .plan-row--family{top:133px}
  .plan-row--business{top:174px}

  .backup-note{position:absolute;left:27px;top:222px;font-family:"Oswald",Arial,sans-serif;font-weight:300;font-size:18px;line-height:25px;color:#111}
  .backup-note strong{display:block;font-weight:400;color:var(--sun);font-size:25px;line-height:34px}

  .store-map{position:absolute;left:218px;top:210px;width:142px;height:142px;border-radius:50%;border:4px solid #fff;
    background:radial-gradient(circle at 45% 50%,#f1eee8 0%,#e2ded6 60%,#cfcac0 100%);box-shadow:0 0 0 1px #b9d9ea}
  .store-map__pin{position:absolute;left:58px;top:52px}

  .info-strip{position:absolute;left:0;top:342px;width:388px;height:66px;background:var(--sky);
    clip-path:polygon(0 0,97% 0,100% 100%,0 100%)}
  .call-box{position:absolute;left:20px;top:338px;width:112px;height:68px;background:var(--ocean);color:#fff;text-align:center;
    font-family:"Oswald",Arial,sans-serif;clip-path:polygon(6% 0,94% 0,100% 12%,100% 88%,94% 100%,6% 100%,0 88%,0 12%)}
  .call-box__label{font-size:17px;line-height:18px;padding-top:4px}
  .call-box__phone{font-size:17px;line-height:20px}
  .call-box__remote{font-size:11px;line-height:12px;font-weight:300;text-transform:uppercase}
  .address{position:absolute;left:150px;top:346px;color:#fff;font-size:14px;line-height:17px;font-style:normal}
  .hours{position:absolute;left:150px;top:414px;font-family:"Oswald",Arial,sans-serif;font-weight:300;font-size:13.5px;color:#222}

  .coast-photo{position:absolute;left:0;top:440px;width:362px;height:106px;
    background:linear-gradient(180deg,#ffffff 0%,#c9dbe6 25%,#6f7d6c 55%,#3d5347 72%,#3d7fa4 86%,#2f6f96 100%)}

  .card--back .brand{left:408px;top:52px}
  .card--back .brand__dot{width:14px;height:14px}
  .card--back .brand__name{font-size:18px}
  .stamp-box{position:absolute;left:611px;top:25px;width:69px;height:76px;border:1px solid #333}
  .island-ghost{position:absolute;left:410px;top:270px;width:290px;height:130px;
    background:radial-gradient(ellipse at 60% 50%,rgba(160,200,230,.45) 0%,rgba(190,220,240,.25) 50%,rgba(255,255,255,0) 75%)}
</style>
</head>
<body>

<section class="card card--front" aria-label="Postcard front">
  <div class="tropic-scene" role="img" aria-label="Tropical beach scene with palm trees and a surfer silhouette"></div>
  <div class="island-chain" role="img" aria-label="Hawaiian island chain"></div>
  <div class="brand"><span class="brand__dot"></span><span class="brand__name">ReefByte</span></div>

  <div class="headline-band"></div>
  <h1 class="headline">We are a PC and Notebook repair shop<br>with full retail services</h1>

  <div class="plan-tab"></div>
  <h2 class="plan-title">SERVICE <span>PLAN</span></h2>

  <ul class="perks">
    <li>Unlimited Virus Removals Only applies to<br>PCs and Notebooks.($139.99Value)</li>
    <li>Unlimited Computer Tune-ups($84.99 Value)</li>
    <li>Kauai Based Company</li>
    <li>Unlimited Device Setups Get your camera.<br>MP3 player or printer setup.</li>
    <li>Includes Internet Security Software($299.99 value)</li>
    <li>Unlimited Troubleshooting On printers. email and software.</li>
    <li>Filtered DNS Service ($49.99/monthValue)</li>
    <li>Unlimited Remote Support ($84.99Value)</li>
    <li>Free Online/Local Backup Software ($99.99 Value)</li>
  </ul>

  <div class="contact-pill contact-pill--phone">
    <svg width="14" height="14" viewBox="0 0 14 14"><circle cx="7" cy="7" r="6" fill="none" stroke="#fff" stroke-width="1.2"/><path d="M4.5 4.2l1.2-.5.8 1.6-.7.6c.4.9 1 1.5 1.9 1.9l.6-.7 1.6.8-.5 1.2c-2.6-.2-4.7-2.3-4.9-4.9z" fill="#fff"/></svg>
    808-519-3371
  </div>
  <div class="contact-pill contact-pill--web">
    <svg width="13" height="13" viewBox="0 0 13 13" fill="none" stroke="#fff" stroke-width="1"><circle cx="6.5" cy="6.5" r="5.5"/><ellipse cx="6.5" cy="6.5" rx="2.4" ry="5.5"/><path d="M1 6.5h11"/></svg>
    www.reefbyteshop.com
  </div>
</section>

<section class="card card--back" aria-label="Postcard back">
  <svg class="back-shape" width="705" height="546" viewBox="0 0 705 546">
    <path d="M0 0H322C372 45 392 120 388 200V342H0Z" fill="#cfeefb"/>
    <path d="M322 0H340C392 45 412 120 408 200V346H388V200C392 120 372 45 322 0Z" fill="#1fa6e4"/>
  </svg>

  <p class="offer-intro">We offer a bunch of<br>different service contract<br>options for our customers:</p>

  <div class="plan-row plan-row--single"><span class="plan-row__name">Single Computer</span><span class="plan-row__price">24.99/month</span></div>
  <div class="plan-row plan-row--family"><span class="plan-row__name">Family Plan</span><span class="plan-row__price">29.99/month</span></div>
  <div class="plan-row plan-row--business"><span class="plan-row__name">Business Plan</span><span class="plan-row__price">49.99/computer month</span></div>

  <p class="backup-note">We Also Offer Backup Services<br>Much Like Vaultwisp<br>But Our Own Brand Starting<strong>At 9.99/month.</strong></p>

  <div class="store-map" role="img" aria-label="Plorin street map marking the store location">
    <svg class="store-map__pin" width="14" height="20" viewBox="0 0 14 20"><path d="M7 0C3 0 0 3 0 7c0 5 7 13 7 13s7-8 7-13c0-4-3-7-7-7z" fill="#d9342b"/><circle cx="7" cy="7" r="2.5" fill="#fff"/></svg>
  </div>

  <div class="info-strip"></div>
  <div class="call-box">
    <div class="call-box__label">CALL NOW</div>
    <div class="call-box__phone">808-519-3371</div>
    <div class="call-box__remote">Remote Services<br>808-519-3371 x1</div>
  </div>
  <address class="address">ReefByte LLC.<br>1845 Kaumualii Hwy Suite 210<br>Lihue, Hawaii 96766</address>
  <p class="hours">Store hours mon - friday 9am - 6pm</p>

  <div class="coast-photo" role="img" aria-label="Kauai coastline cliffs with a kayaker on the sea"></div>

  <div class="brand"><span class="brand__dot"></span><span class="brand__name">ReefByte</span></div>
  <div class="stamp-box"></div>
  <div class="island-ghost" role="img" aria-label="Faint outline of the Hawaiian islands"></div>
</section>

</body>
</html>
```